Business Card Design Project

We need a business card to reflect the design of our website - just so it all ties in - it has a retro feel and can be found at http://www.velorasoulpair.com
We will need our phone 0437 215 964
Web address, and email velorapair@fernmail.com included
Our catch cry is "Classic Cocktail Music"
Perfect Live Music for Private & Corporate Events, Weddings and Dinner Music
Our names should be included :-
Maribel Thorne / piano & Dennis Holloway / bass
I am now also including our logo so that it can be included (in part or whole) somehow in the design
My partner thinks we should include our logo in some form in the design of the card - i will attach this here for you. I will attach eps but if you prefer another format please let me know
Regards
Mari

```html
<!DOCTYPE html>
<html lang="en">
<head>
<meta charset="utf-8">
<title>Velora Duo – Business Card</title>
<link rel="stylesheet" href="https://fonts.googleapis.com/css2?family=Poiret+One&family=Fira+Mono:wght@400;500&family=Josefin+Sans:wght@700&display=swap">
<style>
  :root {
    --backdrop: #e9e6e1;
    --card-teal: #8fc0bc;
    --card-teal-dark: #7aaeaa;
    --seam: #6b9f9b;
    --seam-light: #b5d8d4;
    --badge: #4b4b4b;
    --cream: #f3ecd6;
    --ribbon: #efe4c4;
    --ribbon-shade: #d6c79e;
    --ink: #3a3a3a;
    --white: #ffffff;
  }
  * { margin: 0; padding: 0; box-sizing: border-box; }
  html, body { width: 1200px; height: 1000px; overflow: hidden; }
  body { background: var(--backdrop); position: relative; }
  .card {
    position: absolute;
    top: 343px;
    width: 560px;
    height: 314px;
    border-radius: 10px;
    overflow: hidden;
    background: var(--card-teal);
    box-shadow: 0 6px 14px rgba(0,0,0,0.28);
  }
  .card--front { left: 30px; }
  .card--back { left: 610px; }
  .card svg { display: block; width: 560px; height: 314px; }
  .wordmark { font-family: "Poiret One", sans-serif; font-size: 38px; fill: var(--cream); letter-spacing: 1px; }
  .tagline { font-family: "Josefin Sans", sans-serif; font-weight: 700; font-size: 10px; fill: var(--ink); letter-spacing: 0.5px; }
  .contact-text { font-family: "Fira Mono", monospace; font-size: 16px; fill: var(--white); }
  .badge-name { font-family: "Poiret One", sans-serif; font-size: 22px; fill: var(--cream); }
  .members { font-family: "Fira Mono", monospace; font-weight: 500; font-size: 15.5px; fill: var(--white); }
</style>
</head>
<body>

<!-- Front side -->
<div class="card card--front">
  <svg viewBox="0 0 560 314" aria-label="Front of business card">
    <!-- upper panel with notch around badge -->
    <path d="M0 0 H560 V128 H170 A81 81 0 0 1 8 128 H0 Z" fill="var(--card-teal)"/>
    <path d="M0 128 H8 A81 81 0 0 0 170 128 H560" fill="none" stroke="var(--seam)" stroke-width="1.5"/>
    <path d="M0 131 H8 A81 81 0 0 0 170 131 H560" fill="none" stroke="var(--seam-light)" stroke-width="1" opacity="0.7"/>
    <path d="M0 139 H14 A76 76 0 0 0 164 139 H560" fill="none" stroke="var(--seam)" stroke-width="1" stroke-dasharray="4 3"/>
    <line x1="178" y1="120" x2="560" y2="120" stroke="var(--seam)" stroke-width="1" stroke-dasharray="4 3"/>

    <!-- badge -->
    <circle class="badge" cx="89" cy="80" r="63" fill="var(--badge)" stroke="var(--cream)" stroke-width="2"/>

    <!-- name and tagline -->
    <text class="wordmark" x="351" y="62" text-anchor="middle">VELORA DUO</text>
    <line x1="186" y1="88" x2="262" y2="88" stroke="var(--cream)" stroke-width="2" stroke-dasharray="1 6" stroke-linecap="round"/>
    <line x1="440" y1="88" x2="516" y2="88" stroke="var(--cream)" stroke-width="2" stroke-dasharray="1 6" stroke-linecap="round"/>
    <g class="ribbon">
      <path d="M270 78 L430 74 L432 98 L272 102 Z" fill="var(--ribbon)"/>
      <path d="M270 78 L262 92 L272 102 Z" fill="var(--ribbon-shade)"/>
      <path d="M430 74 L440 86 L432 98 Z" fill="var(--ribbon-shade)"/>
      <text class="tagline" x="351" y="92" text-anchor="middle">CLASSIC COCKTAIL MUSIC</text>
    </g>

    <!-- contact details -->
    <g class="contact">
      <circle cx="240" cy="191" r="10" fill="var(--white)"/>
      <path d="M235 185 q-1 3 2 8 q3 4 7 5 l2-2 -3-3 -2 1 q-3-2-4-5 l1-2 -3-3 z" fill="var(--card-teal-dark)"/>
      <text class="contact-text" x="258" y="197">0437 215 964</text>

      <circle cx="240" cy="223" r="10" fill="var(--white)"/>
      <rect x="234" y="218.5" width="12" height="9" rx="1" fill="var(--card-teal-dark)"/>
      <path d="M234 219 L240 224 L246 219" fill="none" stroke="var(--white)" stroke-width="1.2"/>
      <text class="contact-text" x="258" y="229">velorapair@fernmail.com</text>

      <circle cx="240" cy="254" r="10" fill="var(--white)"/>
      <g fill="none" stroke="var(--card-teal-dark)" stroke-width="1.2">
        <circle cx="240" cy="254" r="6.5"/>
        <ellipse cx="240" cy="254" rx="3" ry="6.5"/>
        <line x1="233.5" y1="254" x2="246.5" y2="254"/>
        <line x1="235" y1="250.5" x2="245" y2="250.5"/>
        <line x1="235" y1="257.5" x2="245" y2="257.5"/>
      </g>
      <text class="contact-text" x="258" y="260">www.velorasoulpair.com</text>
    </g>
  </svg>
</div>

<!-- Back side -->
<div class="card card--back">
  <svg viewBox="0 0 560 314" aria-label="Back of business card">
    <circle cx="280" cy="133" r="82" fill="var(--badge)" stroke="var(--cream)" stroke-width="2"/>
    <text class="badge-name" x="280" y="141" text-anchor="middle">Velora Duo</text>

    <line x1="0" y1="250" x2="560" y2="250" stroke="var(--seam)" stroke-width="1" stroke-dasharray="4 3"/>
    <line x1="0" y1="252" x2="560" y2="252" stroke="var(--seam-light)" stroke-width="1" opacity="0.6"/>
    <line x1="0" y1="280" x2="560" y2="280" stroke="var(--seam)" stroke-width="1" stroke-dasharray="4 3"/>
    <text class="members" x="280" y="270" text-anchor="middle">Maribel Thorne / piano &amp; Dennis Holloway / bass</text>
  </svg>
</div>

</body>
</html>
```